Business card design needed

Our modern electrical contracting company requires business card design utilising our logo and incorporating our tag line "Service when you need it". We specialise in assisting our customers 24/7 offering a breakdown service.

Industry/Entity Type

Electrical

Contact Information for Business Card

Marcus Penhale, Electrical contractor,Tel: (08) 8456 3071, Fax: (08) 8679 4315, Mob 0438 562 740, Email: marcus.penhale@brightwirepower.com.au, Web: www.brightwirepower.com.au

Requirements
Must have
• we require a 2 sided card.
Front- Logo, tag line and contact information.
Rear- service when you need it! Call now for our 24/7 breakdown service

```html
<!DOCTYPE html>
<html lang="en">
<head>
<meta charset="utf-8">
<title>Brightwire Power – Business Card</title>
<link href="https://fonts.googleapis.com/css2?family=Iceland&family=PT+Sans:wght@400;700&display=swap" rel="stylesheet">
<style>
  :root {
    --page-bg: #e9e7e4;
    --card-dark: #3a3637;
    --card-light: #ffffff;
    --ink-light: #f2f2f2;
    --ink-grey: #8b8b8b;
    --ink-soft: #9a9a9a;
    --rule: #d6d6d6;
    --brand-blue: #24409a;
  }
  * { box-sizing: border-box; margin: 0; padding: 0; }
  html, body {
    width: 1200px; height: 1000px; overflow: hidden;
    background: var(--page-bg);
  }
  .sheet {
    position: relative; width: 1200px; height: 1000px;
    display: flex; flex-direction: column; align-items: center;
    justify-content: center; gap: 60px;
  }
  .card {
    position: relative; width: 620px; height: 379px;
    box-shadow: 0 6px 18px rgba(0,0,0,0.18);
  }
  /* Rear side */
  .card--rear {
    background: var(--card-dark);
    display: flex; flex-direction: column; align-items: center; justify-content: center;
  }
  .tagline {
    font-family: "Iceland", sans-serif;
    color: var(--ink-light);
    font-size: 21px; letter-spacing: 4px; line-height: 1.15;
    text-transform: uppercase; text-align: center;
  }
  /* Front side */
  .card--front { background: var(--card-light); }
  .divider {
    position: absolute; left: 0; top: 0;
  }
  .contact-block {
    position: absolute; left: 52px; top: 92px;
    font-family: "PT Sans", sans-serif;
  }
  .contact-name {
    color: var(--ink-grey); font-size: 40px; font-weight: 400; line-height: 1;
  }
  .contact-role {
    color: var(--ink-grey); font-size: 23px; margin: 4px 0 0 14px; line-height: 1;
  }
  .contact-list {
    list-style: none; margin: 22px 0 0 34px;
  }
  .contact-list li {
    display: flex; align-items: center; gap: 10px;
    color: var(--ink-soft); font-size: 13.5px; height: 20px;
  }
  .contact-list svg { width: 14px; height: 14px; flex: none; }
  .brand {
    position: absolute; left: 350px; top: 0; width: 270px; height: 379px;
    display: flex; flex-direction: column; align-items: center; justify-content: center; gap: 10px;
  }
  .brand-dot {
    width: 52px; height: 52px; border-radius: 50%; background: var(--brand-blue);
  }
  .brand-name {
    font-family: "PT Sans", sans-serif; font-weight: 700;
    color: var(--brand-blue); font-size: 23px; text-transform: uppercase; letter-spacing: 0.5px;
  }
</style>
</head>
<body>
<main class="sheet">
  <section class="card card--rear" aria-label="Card rear">
    <p class="tagline">Service when you need it!<br>Call now for our 24/7 breakdown service.</p>
  </section>

  <section class="card card--front" aria-label="Card front">
    <svg class="divider" width="620" height="379" viewBox="0 0 620 379" aria-hidden="true">
      <line x1="332" y1="0" x2="372" y2="379" stroke="var(--rule)" stroke-width="1.5"/>
    </svg>

    <div class="contact-block">
      <h1 class="contact-name">Marcus Penhale</h1>
      <p class="contact-role">Electrical contractor</p>
      <ul class="contact-list">
        <li>
          <svg viewBox="0 0 16 16" aria-label="Telephone"><path d="M4 1.5 6.2 4 5 5.6c.8 2 2.4 3.6 4.4 4.4L11 8.8l2.5 2.2-1.4 2.5C7 13.2 2.8 9 2.5 3.9Z" fill="var(--ink-soft)"/></svg>
          (08) 8456 3071
        </li>
        <li>
          <svg viewBox="0 0 16 16" aria-label="Fax"><rect x="4" y="1.5" width="8" height="4" fill="none" stroke="var(--ink-soft)" stroke-width="1.3"/><rect x="1.5" y="5.5" width="13" height="6" rx="1" fill="var(--ink-soft)"/><rect x="4" y="10" width="8" height="4.5" fill="#fff" stroke="var(--ink-soft)" stroke-width="1.3"/></svg>
          (08) 8679 4315
        </li>
        <li>
          <svg viewBox="0 0 16 16" aria-label="Mobile"><rect x="4.5" y="1.5" width="7" height="13" rx="1.3" fill="none" stroke="var(--ink-soft)" stroke-width="1.4"/><circle cx="8" cy="12" r="0.9" fill="var(--ink-soft)"/></svg>
          0438 562 740
        </li>
        <li>
          <svg viewBox="0 0 16 16" aria-label="Email"><rect x="1.5" y="3.5" width="13" height="9" fill="none" stroke="var(--ink-soft)" stroke-width="1.3"/><path d="M1.5 3.5 8 9l6.5-5.5" fill="none" stroke="var(--ink-soft)" stroke-width="1.3"/></svg>
          marcus.penhale@brightwirepower.com.au
        </li>
        <li>
          <svg viewBox="0 0 16 16" aria-label="Website"><circle cx="8" cy="8" r="6.3" fill="none" stroke="var(--ink-soft)" stroke-width="1.2"/><ellipse cx="8" cy="8" rx="2.8" ry="6.3" fill="none" stroke="var(--ink-soft)" stroke-width="1.1"/><line x1="1.7" y1="8" x2="14.3" y2="8" stroke="var(--ink-soft)" stroke-width="1.1"/></svg>
          www.brightwirepower.com.au
        </li>
      </ul>
    </div>

    <div class="brand">
      <span class="brand-dot" aria-hidden="true"></span>
      <span class="brand-name">Brightwire Power</span>
    </div>
  </section>
</main>
</body>
</html>
```